Business Card Design Project - ol taviran group

dear Sirs

we need business card design for our group ( OL Taviran Group ) , i have got the Logo design of our group from pixel forum in previous , so all need details relating to our group i think available with you, as well as the the chosen logo design

we hope to provide us with business card logo that to be appropaite and satisfactory to us .

thanks

note : logo design of our group is attached .

Reason: please extend the deadline of my project for additional 15 days because i didn't received appropriate design for our gruop yet . kindly beaware that i have received 77 design till now , supossed to send me 200-250 design at least . thanks

contents

name : Selim OR Haddani

position : Operation Manager

• person name

group logo
• logo color matching with back background

```html
<!DOCTYPE html>
<html lang="en">
<head>
<meta charset="utf-8">
<title>OL Taviran Group – Business Card</title>
<link rel="stylesheet" href="https://fonts.googleapis.com/css2?family=Jost:wght@400;500;600;700&display=swap">
<style>
  :root {
    --brand-blue: #0b4a8b;
    --brand-gold: #b58b2b;
    --card-white: #fbfbfb;
    --backdrop: #e4e4e2;
    --text-white: #ffffff;
  }
  * { margin: 0; padding: 0; box-sizing: border-box; }
  html, body {
    width: 1200px; height: 792px; overflow: hidden;
    background: var(--backdrop);
    font-family: "Jost", "Futura", sans-serif;
  }
  .canvas {
    position: relative; width: 1200px; height: 792px;
    display: flex; align-items: center; justify-content: center; gap: 40px;
  }
  .card {
    position: relative; width: 530px; height: 303px; overflow: hidden;
    box-shadow: 0 6px 18px rgba(0,0,0,0.18);
  }

  /* Front */
  .card-front { background: var(--card-white); }
  .front-top-band { position: absolute; top: 0; left: 0; right: 0; height: 10px; background: var(--brand-gold); }
  .front-bottom-band { position: absolute; bottom: 0; left: 0; right: 0; height: 12px; background: var(--brand-blue); }
  .front-brand {
    position: absolute; top: 52px; left: 34px;
    display: flex; align-items: center; gap: 10px;
    color: var(--brand-blue); font-weight: 500; font-size: 22px; letter-spacing: 0.5px;
    white-space: nowrap;
  }
  .brand-square { width: 18px; height: 18px; background: var(--brand-blue); flex: none; }
  .person { position: absolute; top: 30px; right: 34px; text-align: right; white-space: nowrap; }
  .person-name { color: var(--brand-blue); font-size: 22px; font-weight: 400; line-height: 1.2; }
  .person-title { color: var(--brand-gold); font-size: 14px; font-weight: 600; }
  .contact-list {
    position: absolute; list-style: none; line-height: 1.35;
  }
  .contact-list li { display: flex; align-items: baseline; gap: 6px; white-space: nowrap; }
  .contact-label { color: var(--brand-gold); font-weight: 600; font-size: 13.5px; flex: none; }
  .contact-value { color: var(--brand-blue); }
  .contact-online { top: 150px; right: 34px; font-size: 14.5px; }
  .contact-online .contact-label { width: 72px; text-align: right; }
  .contact-phone { bottom: 34px; left: 34px; font-size: 16px; }
  .contact-phone .contact-label { width: 44px; }

  /* Back */
  .card-back { background: var(--brand-blue); }
  .back-brand {
    position: absolute; top: 78px; left: 0; right: 0;
    display: flex; align-items: center; justify-content: center; gap: 14px;
    color: var(--text-white); font-weight: 500; font-size: 40px; letter-spacing: 1px;
    white-space: nowrap;
  }
  .back-brand .brand-square { width: 28px; height: 28px; background: var(--text-white); }
  .back-band {
    position: absolute; left: 0; right: 0; bottom: 0; height: 62px;
    background: var(--brand-gold);
    display: flex; align-items: center; justify-content: center;
  }
  .back-url { color: var(--text-white); font-size: 18px; letter-spacing: 2.5px; font-weight: 400; white-space: nowrap; }
  .back-url strong { font-weight: 700; }
</style>
</head>
<body>
<main class="canvas">
  <section class="card card-front" aria-label="Card front">
    <div class="front-top-band"></div>
    <div class="front-brand"><span class="brand-square"></span><span>OL Taviran Group</span></div>
    <div class="person">
      <p class="person-name">Selim OR Haddani</p>
      <p class="person-title">Operation Manager</p>
    </div>
    <ul class="contact-list contact-online">
      <li><span class="contact-label">Email :</span><span class="contact-value">selim@oltavirangroup.com</span></li>
      <li><span class="contact-label">Website :</span><span class="contact-value">oltavirangroup.com</span></li>
      <li><span class="contact-label">PO. Box :</span><span class="contact-value">Your PO Box Number</span></li>
    </ul>
    <ul class="contact-list contact-phone">
      <li><span class="contact-label">Tel :</span><span class="contact-value">+00 123 456 789</span></li>
      <li><span class="contact-label">Fax :</span><span class="contact-value">+00 123 456 789</span></li>
      <li><span class="contact-label">Mob :</span><span class="contact-value">+00 123 456 789</span></li>
    </ul>
    <div class="front-bottom-band"></div>
  </section>

  <section class="card card-back" aria-label="Card back">
    <div class="back-brand"><span class="brand-square"></span><span>OL Taviran Group</span></div>
    <div class="back-band">
      <p class="back-url">www.<strong>oltavirangroup</strong>.com</p>
    </div>
  </section>
</main>
</body>
</html>
```